Outdoor sign for Brightwater Auto Restoration

I need a horizontal 4'x 8' outdoor roadside sign for my classic auto restoration business. I have uploaded colors and our logo. Needs the Brightwater name, a prominent Classic AUTO RESTORATION, phone number and website. We rebuild and restore vintage cars, trucks and 4x4s. I'd like something clean but possibly retro. Classic Auto Restoration is more important than the Brightwater name. It needs to be visible and readable from the street. NO CLIP ART

Target Market(s)

Customers who need their vintage care restored or upgraded. Men and women ages 25-75

Industry/Entity Type

Automotive

Colors
FFC000
F8CF3A
FAE287
FDF2CF
FEFAEE

Requirements
Must have
• Legible. Bright. Readable as a backlit 4' x 8' large horizontal sign (roughly 120cm X 240cm)
Nice to have
• Use of the Brightwater logo/type, Complete or Classic before prominent AUTO RESTORATION
Should not have
• Clip art of old cars or icons. And we don't want the Brightwater Logo from the website because it wont be legible from the road. I have included the Illustrator file for Brightwater text in the uploads

```html
<!DOCTYPE html>
<html lang="en">
<head>
<meta charset="utf-8">
<title>Brightwater Auto Restoration – Roadside Sign</title>
<link href="https://fonts.googleapis.com/css2?family=Oswald:wght@600;700&display=swap" rel="stylesheet">
<style>
  :root {
    --backdrop: #9b9b9b;
    --cream: #fff0d6;
    --band-orange: #cf6612;
    --dot-gold: #ffb33a;
    --name-gold: #f7a51c;
    --headline-orange: #c9621a;
    --contact-gold: #b9851a;
    --star-gold: #ffc94a;
    --car-navy: #0f1a3a;
  }
  * { margin: 0; padding: 0; box-sizing: border-box; }
  html, body { width: 1072px; height: 1200px; overflow: hidden; }
  body { background: var(--backdrop); position: relative; font-family: "Oswald", "Arial Narrow", sans-serif; }

  .sign {
    position: absolute; left: 36px; top: 350px;
    width: 1000px; height: 500px;
    background: var(--cream);
    overflow: hidden;
  }
  .sign-art { position: absolute; inset: 0; width: 1000px; height: 500px; }

  .brand-name {
    position: absolute; left: 0; right: 0; top: 6px;
    text-align: center; font-weight: 700; font-size: 42px; line-height: 52px;
    color: var(--name-gold); letter-spacing: 0.5px;
  }
  .headline {
    position: absolute; left: 0; right: 0; top: 68px;
    text-align: center; font-weight: 700; font-size: 66px; line-height: 76px;
    color: var(--headline-orange); letter-spacing: -0.5px;
  }
  .vehicle-illustration {
    position: absolute; left: 180px; top: 170px; width: 612px; height: 228px;
    border-radius: 120px 110px 30px 40px;
    background: linear-gradient(180deg, #1c2850 0%, var(--car-navy) 100%);
  }
  .contact {
    position: absolute; top: 410px; font-weight: 600; font-size: 45px; line-height: 50px;
    color: var(--contact-gold); letter-spacing: -0.5px;
  }
  .contact-phone { left: 70px; }
  .contact-web { right: 72px; }
</style>
</head>
<body>
  <section class="sign">
    <svg class="sign-art" viewBox="0 0 1000 500" aria-hidden="true">
      <defs>
        <symbol id="star" viewBox="-10 -10 20 20">
          <polygon points="0,-10 2.35,-3.24 9.51,-3.09 3.8,1.24 5.88,8.09 0,4 -5.88,8.09 -3.8,1.24 -9.51,-3.09 -2.35,-3.24"/>
        </symbol>
        <pattern id="band-dots" patternUnits="userSpaceOnUse" x="16" y="0" width="34" height="63">
          <circle cx="17" cy="31.5" r="6" fill="var(--dot-gold)"/>
        </pattern>
        <pattern id="band-stars" patternUnits="userSpaceOnUse" x="0" y="459" width="55.5" height="41">
          <use href="#star" x="17.5" y="10.5" width="20" height="20" fill="var(--star-gold)"/>
        </pattern>
      </defs>

      <rect class="top-band" x="0" y="0" width="1000" height="63" fill="var(--band-orange)"/>
      <rect x="16" y="0" width="340" height="63" fill="url(#band-dots)"/>
      <rect x="662" y="0" width="340" height="63" fill="url(#band-dots)"/>

      <g class="headline-stars" fill="none" stroke="var(--headline-orange)" stroke-width="1.3">
        <use href="#star" x="39" y="85" width="34" height="34"/>
        <use href="#star" x="186" y="90" width="25" height="25"/>
        <use href="#star" x="776" y="90" width="25" height="25"/>
        <use href="#star" x="912" y="85" width="34" height="34"/>
      </g>

      <rect class="bottom-band" x="0" y="459" width="1000" height="41" fill="var(--band-orange)"/>
      <rect x="0" y="459" width="1000" height="41" fill="url(#band-stars)"/>
    </svg>

    <div class="brand-name">BRIGHTWATER</div>
    <h1 class="headline">AUTO RESTORATION</h1>
    <div class="vehicle-illustration" role="img" aria-label="Navy side-profile illustration of a vintage sedan with whitewall tires"></div>
    <div class="contact contact-phone">501-555-0142</div>
    <div class="contact contact-web">brightwater autoworks.com</div>
  </section>
</body>
</html>
```